Resturant Menu Design

Kindly design two menus for our restaurant. The first one will be an A4 size foldable Menu that will be given to people pacing and order and sitting in while the second one will be folded short menu for Take Aways. Some of the pictures of the menus are uploaded but not all menu items have pictures.

Target Market(s)

Corporate Dinners

Industry/Entity Type

Restaurant

```html
<!DOCTYPE html>
<html lang="en">
<head>
<meta charset="utf-8">
<title>Menu – Wraps, Pizzas, Salads &amp; Burgers</title>
<link href="https://fonts.googleapis.com/css2?family=Alegreya+Sans+SC:wght@700;800&family=Roboto+Condensed:wght@300;400&family=Sancreek&display=swap" rel="stylesheet">
<style>
  :root {
    --maroon: #8c1d2f;
    --ink: #1f1f1f;
    --desc: #333333;
    --panel: #ffffff;
    --board-light: #f3f3f1;
    --board-dark: #dcdcda;
  }
  * { margin: 0; padding: 0; box-sizing: border-box; }
  html, body { width: 849px; height: 1200px; overflow: hidden; }
  body {
    position: relative;
    background: linear-gradient(90deg, var(--board-light), var(--board-dark) 30%, var(--board-light) 55%, var(--board-dark) 80%, var(--board-light));
    font-family: "Roboto Condensed", sans-serif;
    color: var(--ink);
  }
  .panel {
    position: absolute; left: 51px; top: 51px; width: 745px; height: 1160px;
    background: rgba(255,255,255,0.88);
    border: 1.5px solid var(--maroon);
  }
  .section-title {
    position: absolute;
    font-family: "Sancreek", serif;
    font-weight: 400;
    color: var(--maroon);
    font-size: 34px; line-height: 1;
    text-transform: uppercase;
    letter-spacing: 1px;
  }
  .section-title small {
    font-family: "Roboto Condensed", sans-serif;
    font-weight: 300; font-size: 12px; color: var(--desc);
    text-transform: none; letter-spacing: 0;
  }
  .dots {
    position: absolute; height: 0;
    border-top: 3px dotted var(--maroon);
  }
  .item { position: absolute; }
  .item .name {
    font-family: "Alegreya Sans SC", sans-serif;
    font-weight: 700; font-size: 17px; line-height: 14px;
    letter-spacing: 0.6px; color: var(--ink);
    padding-top: 2px;
  }
  .item .desc {
    font-weight: 300; font-size: 12.2px; line-height: 14px; color: var(--desc);
    margin-top: 1px;
  }
  .item .price, .item .prices {
    position: absolute; right: 0; bottom: 0;
    font-weight: 300; font-size: 12.2px; line-height: 14px; color: var(--desc);
  }
  .item .prices span { display: inline-block; width: 52px; text-align: right; }
  .spice {
    font-family: "Roboto Condensed", sans-serif; font-weight: 300; font-size: 12px;
  }
  .size-head {
    position: absolute; top: 120px; left: 688px;
    font-family: "Alegreya Sans SC", sans-serif; font-weight: 700; font-size: 13px;
  }
  .size-head span { display: inline-block; width: 52px; }
  .wrap-col { left: 67px; width: 349px; }
  .salad-col { left: 437px; width: 347px; }
  .burger-left { left: 64px; width: 346px; }
  .burger-right { left: 447px; width: 338px; }
  .photos { position: absolute; left: 0; top: 0; }
</style>
</head>
<body>
  <div class="panel"></div>

  <!-- Wraps -->
  <h2 class="section-title" style="left:174px; top:60px;">Wraps</h2>
  <div class="dots" style="left:67px; top:100px; width:352px;"></div>

  <div class="item wrap-col" style="top:118px;"><div class="name">Grilled Chicken, Tomato<br>&amp; Mozzarella Cheese</div><div class="price">R58-00</div></div>
  <div class="item wrap-col" style="top:152px;"><div class="name">Grilled Chicken, Bacon, Feta,<br>Avocado, Pesto</div><div class="price">R60-00</div></div>
  <div class="item wrap-col" style="top:186px;"><div class="name">Cajun Spiced</div><div class="desc">Chicken, Gherkins, Tomato, Avocado<br>&amp; Basil Pesto Mayo</div><div class="price">R62-00</div></div>
  <div class="item wrap-col" style="top:235px;"><div class="name">Hawaiian</div><div class="desc">Bacon, Mozzarella Cheese, Pineapple,<br>Lettuce &amp; Sweet Chili Sauce</div><div class="price">R60-00</div></div>
  <div class="item wrap-col" style="top:283px;"><div class="name">Cajun Wrap</div><div class="desc">Cajun Chicken, Avocado, Tomato, Bacon,<br>Gherkins, Basil Mayo, Chilies, Feta Cheese</div><div class="price">R78-00</div></div>
  <div class="item wrap-col" style="top:332px;"><div class="name">Beef Wrap</div><div class="desc">Marinated Beef Strips, Feta Cheese, Olives,<br>Cucumber, Shredded Lettuce &amp; Tzatziki Sauce</div><div class="price">R74-00</div></div>
  <div class="item wrap-col" style="top:380px;"><div class="name">Beef Quesadilla</div><div class="desc">Beef Strips, Cheddar Cheese, Mozzarella Cheese,<br>Onions &amp; Tomato</div><div class="price">R60-00</div></div>
  <div class="item wrap-col" style="top:429px;"><div class="name">Healthy Wrap</div><div class="desc">Grilled Brinjals, Rocket, Roasted Vegetables,<br>Pesto &amp; Mozzarella Cheese</div><div class="price">R60-00</div></div>

  <!-- Pizzas -->
  <div class="dots" style="left:67px; top:495px; width:352px;"></div>
  <h2 class="section-title" style="left:164px; top:516px;">Pizzas <small>{Standard}</small></h2>
  <div class="item wrap-col" style="top:565px;"><div class="name">Chicken &amp; Mushrooms</div><div class="desc">Creamed Chicken , Mushrooms,<br>Sweet BBQ Tomato Sauce, Mozzarella Cheese</div><div class="price">R64-00</div></div>
  <div class="item wrap-col" style="top:613px;"><div class="name">3 Cheese Pizza (V)</div><div class="desc">Cheddar Cheese, Mozzarella Cheese, Feta Cheese,<br>Sweet Mayo Sauce</div><div class="price">R46-00</div></div>

  <!-- Salads -->
  <h2 class="section-title" style="left:543px; top:60px;">Salads</h2>
  <div class="dots" style="left:437px; top:100px; width:347px;"></div>
  <div class="size-head"><span>Half</span><span>Full</span></div>

  <div class="item salad-col" style="top:116px;"><div class="name">Garden Salad</div><div class="desc">Lettuce, Cucumber, Tomato,<br>Onions &amp; Mixed Peppers</div><div class="prices"><span>R32-00</span><span>R48-00</span></div></div>
  <div class="item salad-col" style="top:179px;"><div class="name">Marisol’s Salad</div><div class="desc">Tuna, Boiled Egg, Lettuce, Cucumber, Tomato,<br>Mixed Peppers, Olives &amp;Onions,</div><div class="prices"><span>R50-00</span><span>R72-00</span></div></div>
  <div class="item salad-col" style="top:242px;"><div class="name">Greek Salad</div><div class="desc">Feta Cheese, Olives, Lettuce, Cucumber,<br>Tomato, Mixed Peppers &amp;Onions</div><div class="prices"><span>R40-00</span><span>R60-00</span></div></div>
  <div class="item salad-col" style="top:305px;"><div class="name">Chef Salad</div><div class="desc">Ham or Bacon, Mozzarella Cheese, Lettuce,<br>Cucumber, Tomato &amp; Onions</div><div class="prices"><span>R45-00</span><span>R72-00</span></div></div>
  <div class="item salad-col" style="top:367px;"><div class="name">Chicken Salad</div><div class="desc">Grilled Chicken, Mozzarella Cheese, Avocado, Lettuce,<br>Cucumber, Tomato &amp; Onions</div><div class="prices"><span>R45-00</span><span>R72-00</span></div></div>
  <div class="item salad-col" style="top:430px;"><div class="name">Chicken And Feta Salad</div><div class="desc">Grilled Chicken, Feta Cheese, Lettuce, Cucumber,<br>Tomato &amp; Onions , Served With Sweet Chili Mayo Sauce<br>&nbsp;</div><div class="prices"><span>R49-00</span><span>R74-00</span></div></div>
  <div class="item salad-col" style="top:493px;"><div class="name">Halloumi Salad</div><div class="desc">Halloumi Cheese, Brinjals, Chickpeas, Olives, Avocado,<br>Lettuce, Cucumber &amp; Tomato With Our Marisol’s Olive Oil &amp; Balsamic<br>Vinegar Dressing</div><div class="prices"><span>R54-00</span><span>R78-00</span></div></div>
  <div class="item salad-col" style="top:570px;"><div class="name">Chicken Liver Salad <span class="spice">{Spicy}</span></div><div class="desc">Chicken Livers, Lettuce, Cucumber, Mixed Peppers, Tomato &amp; Onions<br>Served With Sweet Mustard Dressing</div><div class="prices"><span>R48-00</span><span>R60-00</span></div></div>
  <div class="item salad-col" style="top:632px;"><div class="name">Beef Strips &amp; Beetroot Salad</div><div class="desc">Marinated Beef Strips, Beetroot, Feta Cheese, Lettuce, Cucumber,<br>Tomato &amp; Onions</div><div class="prices"><span>R56-00</span><span>R78-00</span></div></div>

  <!-- Burgers -->
  <div class="dots" style="left:67px; top:689px; width:717px;"></div>
  <h2 class="section-title" style="left:366px; top:702px;">Burgers</h2>

  <div class="item burger-left" style="top:747px;"><div class="name">Plain Beef Burger</div><div class="desc">Beef Patty, Fried Onions, Tomato, Lettuce &amp;<br>Cucumber Served With Chips / Garden Salad</div><div class="price">R55-00</div></div>
  <div class="item burger-left" style="top:795px;"><div class="name">Plain Chicken Burger</div><div class="desc">Chicken Breast, Fried Onions, Tomato, Lettuce &amp;<br>Cucumber Served With Chips / Garden Salad</div><div class="price">R60-00</div></div>
  <div class="item burger-left" style="top:844px;"><div class="name">Beef Cheese Burger</div><div class="desc">Beef Patty , Cheddar Cheese, Cucumber, Lettuce,<br>Tomato, Served With Chips/Garden Salad</div><div class="price">R62-00</div></div>
  <div class="item burger-left" style="top:893px;"><div class="name">Chicken Cheese Burger</div><div class="desc">Chicken breast, Cheddar Cheese, Cucumber, Lettuce,<br>Tomato, Served With Chips / Garden Salad</div><div class="price">R64-00</div></div>

  <div class="item burger-right" style="top:747px;"><div class="name">Double Cheese Beef Burger</div><div class="desc">2 Patties, 1 Patty Cheddar Cheese, 1 Patty Mozzarella Cheese,<br>Onions Rings , Served With Chips / Garden Salad</div><div class="price">R86-00</div></div>
  <div class="item burger-right" style="top:795px;"><div class="name">Schnitzel Burger</div><div class="desc">Chicken Schnitzel, Gherkins, Lettuce, Tomato, Sweet Chili<br>Mayo Sauce Served With Chips / Garden Salad</div><div class="price">R68-00</div></div>
  <div class="item burger-right" style="top:844px;"><div class="name">Bacon, Cheese &amp; Avocado Burger</div><div class="desc">Beef Patty , Bacon, Avocado, Cheese, Lettuce, Cucumber,<br>Tomato, Served With Chips / Garden Salad</div><div class="price">R80-00</div></div>
  <div class="item burger-right" style="top:893px;"><div class="name">Dagwood Burger</div><div class="desc">Beef Patty, Bacon, Fried Egg, 3 Slice Toast, Lettuce, Tomato &amp; Mayo<br>Sauce , Served With Chips / Garden Salad<br>&nbsp;</div><div class="price">R80-00</div></div>

  <!-- Food photo circles -->
  <svg class="photos" width="849" height="1200" viewBox="0 0 849 1200">
    <defs>
      <radialGradient id="wrapTone" cx="40%" cy="40%" r="70%"><stop offset="0" stop-color="#c98a4f"/><stop offset="1" stop-color="#e9b94a"/></radialGradient>
      <radialGradient id="burgerTone" cx="50%" cy="35%" r="70%"><stop offset="0" stop-color="#8a3a1e"/><stop offset="0.6" stop-color="#c7883d"/><stop offset="1" stop-color="#f0cf5e"/></radialGradient>
      <radialGradient id="saladTone" cx="50%" cy="50%" r="70%"><stop offset="0" stop-color="#e7e2c8"/><stop offset="0.6" stop-color="#b8453a"/><stop offset="1" stop-color="#6f8a3c"/></radialGradient>
    </defs>
    <g stroke="var(--maroon)" stroke-width="3">
      <circle cx="104" cy="1118" r="152" fill="#fff"/>
      <circle cx="428" cy="1124" r="164" fill="#fff"/>
      <circle cx="752" cy="1122" r="156" fill="#fff"/>
    </g>
    <circle cx="104" cy="1118" r="144" fill="url(#wrapTone)" role="img" aria-label="Photo of a grilled chicken wrap with chips"/>
    <circle cx="428" cy="1124" r="156" fill="url(#burgerTone)" role="img" aria-label="Photo of a chicken burger with chips"/>
    <circle cx="752" cy="1122" r="148" fill="url(#saladTone)" role="img" aria-label="Photo of a fresh mixed salad with olives and peppers"/>
  </svg>
</body>
</html>
```